Uprising SaaS company needs an attractive business card design

We're an uprising SaaS company who's attempting to attack the rigid car (insurance) claims management market in Europe.
We want to our mighty base order management system, listen to our clients to connect the smart ideas to build something even mightier.
We primarily focus on helping our customers manage their customers' claims/orders and get them resolved as smoothly as possible.
We'd like the business card design to express technical innovation and the fact that we connect smart ideas, as our company slogan indicates.
Contact Information for Business Card
Name, position, website, email, mobile, business address
Font styles to use
Colors
Designer to choose colors to be used in the design.
Look and feel
Each slider illustrates characteristics of the customer's brand and the style your logo design should communicate.

```html
<!DOCTYPE html>
<html lang="en">
<head>
<meta charset="utf-8">
<title>nodewise – business card</title>
<link rel="stylesheet" href="https://fonts.googleapis.com/css2?family=Montserrat:wght@300;400;500;600&display=swap">
<style>
  :root {
    --sky: #84cfe3;
    --paper: #f3f5f4;
    --ink: #6e6e6e;
    --page: #ffffff;
  }
  html, body {
    margin: 0;
    padding: 0;
    width: 1200px;
    height: 1000px;
    overflow: hidden;
    background: var(--page);
    font-family: "Montserrat", sans-serif;
  }
  .card {
    position: absolute;
    left: 317px;
    width: 564px;
    height: 339px;
    background: var(--paper);
    overflow: hidden;
  }
  .card--front { top: 122px; }
  .card--back  { top: 532px; }
  .card svg { display: block; width: 100%; height: 100%; }
  .rule { fill: var(--sky); }
  .band { fill: var(--sky); }
  .stop-sky { stop-color: var(--sky); }
  .stop-paper { stop-color: var(--paper); }
  .brand { font-family: "Montserrat", sans-serif; font-weight: 300; fill: var(--ink); }
  .tagline { font-family: "Montserrat", sans-serif; font-weight: 400; fill: var(--ink); }
  .tagline .accent { fill: var(--sky); }
  .web { font-family: "Montserrat", sans-serif; font-weight: 500; fill: #ffffff; letter-spacing: 1px; }
  .name { font-family: "Montserrat", sans-serif; font-size: 36px; fill: var(--ink); font-weight: 500; letter-spacing: 1px; }
  .name .first { fill: var(--sky); font-weight: 600; }
  .role { font-family: "Montserrat", sans-serif; font-size: 24px; font-weight: 500; fill: var(--sky); letter-spacing: 1px; }
  .contact { font-family: "Montserrat", sans-serif; font-size: 21px; font-weight: 400; fill: var(--ink); letter-spacing: 1px; }
  .icon-dot { fill: var(--sky); }
  .icon-glyph { fill: none; stroke: #ffffff; stroke-width: 2.5; stroke-linecap: round; stroke-linejoin: round; }
  .icon-fill { fill: #ffffff; }
  .globe { fill: none; stroke: #ffffff; stroke-width: 1.6; }
</style>
</head>
<body>

<section class="card card--front" aria-label="Card front">
  <svg viewBox="0 0 988 593" preserveAspectRatio="none">
    <defs>
      <radialGradient id="corner-left" cx="0" cy="0" r="1" gradientUnits="objectBoundingBox">
        <stop offset="0" class="stop-sky"/>
        <stop offset="0.55" class="stop-sky"/>
        <stop offset="1" class="stop-paper"/>
      </radialGradient>
      <radialGradient id="corner-right" cx="1" cy="0" r="1" gradientUnits="objectBoundingBox">
        <stop offset="0" class="stop-sky"/>
        <stop offset="0.55" class="stop-sky"/>
        <stop offset="1" class="stop-paper"/>
      </radialGradient>
    </defs>
    <rect x="0" y="0" width="290" height="292" fill="url(#corner-left)" role="img" aria-label="Decorative wave ornament in sky blue with dashed outline"/>
    <rect x="698" y="0" width="290" height="292" fill="url(#corner-right)" role="img" aria-label="Decorative wave ornament in sky blue with dashed outline"/>

    <rect class="rule" x="439" y="67" width="110" height="6"/>
    <text class="brand" x="494" y="287" text-anchor="middle" font-size="84">nodewise</text>
    <text class="tagline" x="494" y="353" text-anchor="middle" font-size="30">we connect <tspan class="accent">smart ideas</tspan></text>
    <rect class="rule" x="455" y="378" width="78" height="5"/>

    <rect class="band" x="0" y="494" width="988" height="66"/>
    <g transform="translate(357,527)">
      <circle class="globe" r="11"/>
      <ellipse class="globe" rx="5" ry="11"/>
      <line class="globe" x1="-11" y1="0" x2="11" y2="0"/>
      <line class="globe" x1="-9" y1="-6" x2="9" y2="-6"/>
      <line class="globe" x1="-9" y1="6" x2="9" y2="6"/>
    </g>
    <text class="web" x="388" y="535" font-size="22">urwebsitename.com</text>
  </svg>
</section>

<section class="card card--back" aria-label="Card back">
  <svg viewBox="0 0 988 593" preserveAspectRatio="none">
    <defs>
      <linearGradient id="lower-wave" x1="0" y1="0" x2="0" y2="1">
        <stop offset="0" class="stop-paper"/>
        <stop offset="0.45" class="stop-sky"/>
        <stop offset="1" class="stop-sky"/>
      </linearGradient>
    </defs>
    <rect class="band" x="0" y="32" width="988" height="32"/>

    <text class="brand" x="243" y="195" text-anchor="middle" font-size="76">nodewise</text>
    <text class="tagline" x="243" y="245" text-anchor="middle" font-size="24">we connect <tspan class="accent">smart ideas</tspan></text>

    <text class="name" x="895" y="175" text-anchor="end"><tspan class="first">LUKAS</tspan> BRENNER</text>
    <text class="role" x="895" y="214" text-anchor="end">Designation Here</text>
    <rect class="rule" x="816" y="240" width="79" height="5"/>

    <rect x="0" y="290" width="437" height="303" fill="url(#lower-wave)" role="img" aria-label="Decorative wave ornament in sky blue with dashed outline"/>

    <g transform="translate(92,510)">
      <circle class="globe" r="11"/>
      <ellipse class="globe" rx="5" ry="11"/>
      <line class="globe" x1="-11" y1="0" x2="11" y2="0"/>
      <line class="globe" x1="-9" y1="-6" x2="9" y2="-6"/>
      <line class="globe" x1="-9" y1="6" x2="9" y2="6"/>
    </g>
    <text class="web" x="117" y="518" font-size="21">urwebsitename.com</text>

    <text class="contact" x="845" y="404" text-anchor="end">+000 12345 6789</text>
    <g transform="translate(882,396)">
      <circle class="icon-dot" r="13"/>
      <path class="icon-glyph" d="M-5,-6 C-6,0 0,6 6,5 L6,2 L3,0 L1,2 C-1,1 -2,0 -3,-2 L-1,-4 L-3,-7 Z"/>
    </g>

    <text class="contact" x="845" y="450" text-anchor="end">urname@email.com</text>
    <g transform="translate(882,442)">
      <circle class="icon-dot" r="13"/>
      <rect class="icon-glyph" x="-7" y="-4" width="14" height="9" rx="1"/>
      <path class="icon-glyph" d="M-7,-3 L0,2 L7,-3"/>
    </g>

    <text class="contact" x="845" y="490" text-anchor="end">Your Street Address</text>
    <text class="contact" x="845" y="516" text-anchor="end" font-size="19">Singapore, 1234</text>
    <g transform="translate(882,494)">
      <circle class="icon-dot" r="13"/>
      <path class="icon-fill" d="M0,8 C-4,3 -6,0 -6,-2 A6,6 0 0 1 6,-2 C6,0 4,3 0,8 Z"/>
      <circle class="icon-dot" cx="0" cy="-2" r="2.2"/>
    </g>
  </svg>
</section>

</body>
</html>
```